Letterhead and Business Card for Wealth Management Company
Harborline Wealth Management
Letterhead and Business Card for Wealth Management Company - Financial Services
Creative Brief
Use same font as used in my logo
Can use the same font or add additional font
Professional
R. Dwight Voss, CRPC®
Wealth Advisor
2450 Fernbrook Avenue Suite 310 Berwyn, PA 19312
dvoss@harborline-wealth.com
www.harborline-wealth.com
I work with affluent people so I want a sophisticated and classic looking business card and stationary. Our tagline is Dream. Plan. Live. with Live in italics. You can see it on our website at www.harborline-wealth.com. If appropriate, please include the tagline on the business card, letterhead and envelope. Please note the tagline on the website is a gradient color. It looks better printed in solid color.
Be creative.
dvoss dvoss
Thanks for all the great designs! I have a busy schedule today, but I will go through them and give star ratings later today or tonight. Thanks again!
Qwirk Qwirk

```html
<!DOCTYPE html>
<html lang="en">
<head>
<meta charset="utf-8">
<title>Harborline Wealth Management – Business Card</title>
<link rel="stylesheet" href="https://fonts.googleapis.com/css2?family=Open+Sans:ital,wght@0,400;0,600;1,400;1,600&display=swap">
<style>
  :root {
    --canvas: #e6e7e9;
    --card: #ffffff;
    --navy: #16306b;
    --silver: #c9ccd6;
    --silver-soft: #e3e5eb;
    --gold: #c9a24a;
    --ink: #1c2a52;
    --muted: #5a6275;
  }
  * { box-sizing: border-box; margin: 0; padding: 0; }
  html, body {
    width: 1200px; height: 951px; overflow: hidden;
    background: var(--canvas);
    font-family: "Open Sans", Arial, sans-serif;
  }
  .canvas { position: relative; width: 1200px; height: 951px; }
  .card {
    position: absolute; left: 250px; width: 700px; height: 400px;
    background: var(--card); border-radius: 26px; overflow: hidden;
    box-shadow: 0 6px 18px rgba(20, 30, 60, 0.12);
  }
  .card--front { top: 50px; }
  .card--back { top: 501px; }

  .brand {
    position: absolute; display: flex; align-items: center; gap: 14px;
    color: var(--navy); font-weight: 600; letter-spacing: 0.5px;
  }
  .brand__mark { width: 26px; height: 26px; background: var(--gold); flex: none; }
  .card--front .brand { left: 0; right: 0; top: 170px; justify-content: center; font-size: 34px; }
  .card--back .brand { left: 385px; top: 132px; font-size: 22px; width: 290px; gap: 10px; line-height: 1.15; }
  .card--back .brand__mark { width: 20px; height: 20px; }

  .tagline {
    position: absolute; color: var(--gold); font-weight: 600; letter-spacing: 1px;
  }
  .tagline em { font-style: italic; }
  .card--front .tagline { left: 0; right: 0; top: 232px; text-align: center; font-size: 17px; }
  .card--back .tagline { left: 415px; top: 196px; font-size: 13px; }

  .wave { position: absolute; inset: 0; width: 700px; height: 400px; }

  .contact {
    position: absolute; left: 22px; top: 84px; list-style: none;
    color: #ffffff; font-size: 11.5px; line-height: 22px;
  }
  .contact li { display: flex; align-items: center; gap: 8px; }
  .contact__icon { width: 12px; height: 12px; flex: none; }
  .contact .indent { padding-left: 20px; }

  .person { position: absolute; left: 435px; top: 262px; color: var(--ink); }
  .person__name { font-size: 21px; font-weight: 600; }
  .person__title { font-size: 15px; font-style: italic; color: var(--muted); margin-top: 2px; }
</style>
</head>
<body>
<main class="canvas">

  <section class="card card--front" aria-label="Business card front">
    <div class="brand"><span class="brand__mark"></span><span>Harborline Wealth Management</span></div>
    <p class="tagline">Dream. Plan. <em>Live.</em></p>
  </section>

  <section class="card card--back" aria-label="Business card back">
    <svg class="wave" viewBox="0 0 700 400" aria-hidden="true">
      <path d="M0,0 L300,0 C250,110 330,290 470,400 L0,400 Z" fill="var(--silver-soft)"/>
      <path d="M0,0 L270,0 C225,110 300,290 430,400 L0,400 Z" fill="var(--silver)"/>
      <path d="M0,0 L245,0 C200,120 270,290 395,400 L0,400 Z" fill="var(--navy)"/>
      <path d="M318,0 C268,110 350,290 498,400" fill="none" stroke="var(--navy)" stroke-width="2"/>
    </svg>

    <ul class="contact">
      <li><svg class="contact__icon" viewBox="0 0 12 12"><circle cx="6" cy="6" r="6" fill="#fff"/><circle cx="6" cy="5" r="2" fill="var(--navy)"/></svg>2450 Fernbrook Avenue Suite 310</li>
      <li class="indent">Berwyn, PA 19312</li>
      <li><svg class="contact__icon" viewBox="0 0 12 12"><circle cx="6" cy="6" r="6" fill="#fff"/><rect x="3" y="4" width="6" height="4" fill="var(--navy)"/></svg>dvoss@harborline-wealth.com</li>
      <li><svg class="contact__icon" viewBox="0 0 12 12"><circle cx="6" cy="6" r="6" fill="#fff"/><circle cx="6" cy="6" r="2.5" fill="none" stroke="var(--navy)"/></svg>www.harborline-wealth.com</li>
    </ul>

    <div class="brand"><span class="brand__mark"></span><span>Harborline Wealth Management</span></div>
    <p class="tagline">Dream. Plan. <em>Live.</em></p>

    <div class="person">
      <p class="person__name">R. Dwight Voss, CRPC®</p>
      <p class="person__title">Wealth Advisor</p>
    </div>
  </section>

</main>
</body>
</html>
```